Executive recruiting firm in need of business card design

Executive recruiting firm looking for a sleek, classy and modern business card design; card itself will be square shape, rounded edges and soft touch paper, our colors are dark blues in the navy color scale, silvers and grays. Reference our website for a better idea of our company's feel and goals at Staffbrook.com - our company message is "Employee Engagement Begins at Recruitment" this should be on the card

Industry/Entity Type

Business

```html
<!DOCTYPE html>
<html lang="en">
<head>
<meta charset="utf-8">
<title>Staffbrook – Business Card</title>
<link href="https://fonts.googleapis.com/css2?family=Open+Sans:wght@300;400;600;700&display=swap" rel="stylesheet">
<style>
  :root {
    --navy: #2b2c5c;
    --navy-deep: #232449;
    --navy-light: #363875;
    --silver: #dcdde2;
    --silver-muted: #a9aac4;
    --paper: #f4f4f6;
    --paper-shade: #e6e6ea;
    --ink: #2b2c5c;
    --stage: #d9d9dc;
  }
  * { margin: 0; padding: 0; box-sizing: border-box; }
  html, body { width: 1200px; height: 716px; overflow: hidden; }
  body {
    background: var(--stage);
    font-family: "Open Sans", Arial, sans-serif;
    position: relative;
  }
  .card {
    position: absolute;
    top: 213px;
    width: 500px;
    height: 290px;
    border-radius: 22px;
    overflow: hidden;
    box-shadow: 0 6px 18px rgba(0,0,0,0.18);
  }

  /* Front */
  .card--front {
    left: 60px;
    background: linear-gradient(160deg, var(--navy-light) 0%, var(--navy) 55%, var(--navy-deep) 100%);
  }
  .front-brand {
    position: absolute;
    left: 0; right: 0;
    top: 96px;
    text-align: center;
    font-weight: 300;
    font-size: 44px;
    letter-spacing: 2px;
    color: var(--silver);
  }
  .front-message {
    position: absolute;
    left: 0; right: 0;
    top: 164px;
    text-align: center;
    font-size: 12px;
    font-weight: 400;
    letter-spacing: 1.5px;
    color: var(--silver-muted);
  }
  .front-web {
    position: absolute;
    left: 0; right: 0;
    bottom: 42px;
    text-align: center;
    font-size: 13px;
    font-weight: 600;
    color: #e9e9f0;
  }

  /* Back */
  .card--back {
    left: 640px;
    background: linear-gradient(150deg, #ffffff 0%, var(--paper) 55%, var(--paper-shade) 100%);
  }
  .name-block {
    position: absolute;
    left: 26px;
    top: 24px;
    padding-left: 12px;
    border-left: 6px solid var(--navy);
    color: var(--ink);
  }
  .name-block .person { font-size: 20px; font-weight: 400; line-height: 1.1; }
  .name-block .person b { font-weight: 700; }
  .name-block .role { font-size: 11px; }
  .contact-list {
    position: absolute;
    left: 30px;
    top: 96px;
    list-style: none;
    color: var(--ink);
    font-size: 12.5px;
    font-weight: 600;
  }
  .contact-list li {
    display: flex;
    align-items: flex-start;
    gap: 8px;
    margin-bottom: 5px;
    line-height: 1.25;
  }
  .contact-list svg { width: 13px; height: 13px; flex: none; margin-top: 2px; fill: var(--navy); }
  .rule {
    position: absolute;
    left: 0;
    top: 220px;
    width: 340px;
    height: 2px;
    background: var(--navy);
  }
  .back-web {
    position: absolute;
    left: 30px;
    top: 228px;
    font-size: 12.5px;
    font-weight: 600;
    color: var(--ink);
  }
  .back-brand {
    position: absolute;
    right: 34px;
    top: 116px;
    font-weight: 300;
    font-size: 30px;
    letter-spacing: 1.5px;
    color: var(--navy);
  }
  .social-row {
    position: absolute;
    right: 26px;
    top: 213px;
    display: flex;
    gap: 7px;
  }
  .social-row span {
    width: 15px; height: 15px;
    border-radius: 3px;
    background: var(--navy);
  }
</style>
</head>
<body>

<section class="card card--front" aria-label="Card front">
  <div class="front-brand">Staffbrook</div>
  <div class="front-message">Employee Engagement Begins at Recruitment</div>
  <div class="front-web">www.staffbrookgroup.com</div>
</section>

<section class="card card--back" aria-label="Card back">
  <div class="name-block">
    <div class="person">Your <b>Name</b></div>
    <div class="role">Job Title</div>
  </div>

  <ul class="contact-list">
    <li>
      <svg viewBox="0 0 16 16"><path d="M8 0a5.5 5.5 0 0 0-5.5 5.5C2.5 10 8 16 8 16s5.5-6 5.5-10.5A5.5 5.5 0 0 0 8 0zm0 8a2.5 2.5 0 1 1 0-5 2.5 2.5 0 0 1 0 5z"/></svg>
      <span>240 Linden Park Ave.,<br>Oakview, CA</span>
    </li>
    <li>
      <svg viewBox="0 0 16 16"><path d="M1 5c0-2 2-3 7-3s7 1 7 3v1.5h-4V5H5v1.5H1zM3 8h10l1.5 6h-13zM8 9.5a2 2 0 1 0 0 4 2 2 0 0 0 0-4z"/></svg>
      <span>000 000 0000</span>
    </li>
    <li>
      <svg viewBox="0 0 16 16"><path d="M4 1h7v4H4zM1 6h14v9H1zM3 8v2h3V8zm0 3v2h3v-2zm6-3v5h4V8z"/></svg>
      <span>000 000 0000</span>
    </li>
    <li>
      <svg viewBox="0 0 16 16"><path d="M1 3h14v10H1zm1.5 1.5L8 9l5.5-4.5z"/></svg>
      <span>name@staffbrook.com</span>
    </li>
  </ul>

  <div class="rule"></div>
  <div class="back-web">www.staffbrookgroup.com</div>

  <div class="back-brand">Staffbrook</div>

  <div class="social-row" aria-label="Social profiles">
    <span></span><span></span><span></span><span></span><span></span><span></span>
  </div>
</section>

</body>
</html>
```